Flyer design for growing electrical business!!!

looking to get some flyers made for advertising to spread the word about my new business to hopefully create more work!
i am letting potential clients know the type of work i do and am trying to sell my services to them.
To be put on double sided A5. the attached document file has what i would like on each page.
i would like my logo on the first page and and colour scheme of black orange and silver for the flyer following the colours of my logo.
On the second page i would like the photo as a focal point on the top half.
The bold writing are my selling points and would like them accentuated.

```html
<!DOCTYPE html>
<html lang="en">
<head>
<meta charset="utf-8">
<title>Keystone Current Electrical – Flyer</title>
<link href="https://fonts.googleapis.com/css2?family=Roboto:wght@300;400;500;700;900&display=swap" rel="stylesheet">
<style>
  :root{
    --orange:#e9592b;
    --orange-deep:#d94b1f;
    --orange-soft:#ef7a4f;
    --silver:#c8c8c8;
    --black:#1a1a1a;
    --ink:#222;
    --paper:#ffffff;
    --backdrop:#ebe7e1;
  }
  *{box-sizing:border-box;margin:0;padding:0}
  html,body{width:1200px;height:868px;overflow:hidden}
  body{background:var(--backdrop);font-family:"Roboto",Arial,sans-serif;position:relative}
  .flyer{position:absolute;overflow:hidden;box-shadow:0 4px 14px rgba(0,0,0,.25)}
  .abs{position:absolute;left:0;width:100%;text-align:center}

  /* Front */
  .front{left:45px;top:24px;width:545px;height:820px;background:linear-gradient(160deg,#262626,#141414 70%)}
  .brand-mark{position:absolute;left:227px;top:88px;width:92px;height:92px;border-radius:50%;background:var(--orange)}
  .brand-name{top:200px;color:var(--silver);font-weight:700;font-size:44px;letter-spacing:1px;line-height:1}
  .brand-sub{top:252px;color:var(--silver);font-weight:700;font-size:20px;letter-spacing:13px;padding-left:13px}
  .tagline{top:306px;color:#fff;font-size:19px;font-weight:400}
  .tag-rule{position:absolute;left:132px;top:333px;width:290px;height:2px;background:var(--orange)}
  .tagline-sub{top:340px;color:var(--orange);font-size:17px}
  .services{top:374px;color:#fff;font-size:21px;line-height:26px}
  .dot{color:var(--orange)}
  .cta{top:470px;color:var(--orange);font-size:26px;font-weight:300;line-height:27px}
  .cta strong{font-weight:400}
  .service-list{position:absolute;left:0;top:541px;width:100%;display:flex;justify-content:center;font-size:12.6px;line-height:15.4px;color:#eee}
  .service-list ul{list-style:none}
  .service-list .col-left{text-align:right;padding-right:6px}
  .service-list .col-right li::before{content:"• ";color:var(--orange)}
  .contact-name{top:690px;color:var(--orange);font-weight:700;font-size:21px}
  .contact-email{top:716px;color:#fff;font-size:18px}
  .legal{top:768px;color:#ddd;font-size:7.6px;line-height:11px}

  /* Back */
  .back{left:612px;top:42px;width:545px;height:798px;background:var(--paper)}
  .photo{position:absolute;left:0;top:0;width:100%;height:305px;background:linear-gradient(180deg,#e9e9e7 0%,#d6d4d0 55%,#b9b4ad 100%)}
  .logo-plate{position:absolute;left:199px;top:150px;width:134px;height:80px;background:#fff;display:flex;align-items:center;justify-content:center;gap:6px}
  .logo-plate .sq{width:14px;height:14px;background:var(--orange)}
  .logo-plate .name{color:var(--orange);font-weight:700;font-size:12px;line-height:13px;text-align:left}
  .question-band{position:absolute;left:0;top:240px;width:100%;height:100px;background:rgba(233,89,43,.88);color:#fff;font-weight:700;font-size:20.5px;line-height:24px;text-align:center;padding-top:8px}
  .headline{top:352px;color:var(--orange);font-weight:900;font-size:31px;line-height:34px}
  .head-sub{top:423px;color:var(--ink);font-size:13px}
  .head-rule{position:absolute;left:148px;top:448px;width:250px;height:1.5px;background:var(--orange)}
  .pitch{top:460px;color:var(--ink);font-size:12.8px;line-height:22px}
  .table-title{position:absolute;left:42px;top:514px;font-weight:700;font-size:12.6px}
  .table-title.orange{color:var(--orange)}
  .table-title.dark{top:615px;color:var(--ink)}
  .data{position:absolute;left:42px;width:460px;border-collapse:collapse;table-layout:fixed;font-size:8.6px;color:#fff}
  .data td,.data th{height:14px;padding:0 4px;border-bottom:1px solid rgba(255,255,255,.35);text-align:center;font-weight:400}
  .data th{font-weight:700}
  .data.prices{top:531px;background:var(--orange)}
  .data.prices th{background:var(--orange-deep)}
  .data.replace{top:633px;background:var(--black)}
  .data.replace td,.data.replace th{border-bottom-color:#555}
  .more{top:728px;color:var(--ink);font-size:12.6px}
  .light-types{position:absolute;left:0;top:750px;width:100%;display:flex;justify-content:center;font-size:12.6px;line-height:15px;color:var(--ink)}
  .light-types ul{list-style:none}
  .light-types .col-left{text-align:right;padding-right:5px}
  .light-types .col-right li::before{content:"• ";color:var(--orange)}
</style>
</head>
<body>

<section class="flyer front">
  <div class="brand-mark"></div>
  <div class="abs brand-name">KEYSTONE CURRENT</div>
  <div class="abs brand-sub">ELECTRICAL</div>
  <div class="abs tagline">LOCAL ELECTRICIAN IN YOUR AREA</div>
  <div class="tag-rule"></div>
  <div class="abs tagline-sub">FOR ALL YOUR ELECTRICAL NEEDS</div>
  <div class="abs services">
    New installations <span class="dot">•</span> Renovations<br>
    Additions <span class="dot">•</span> Upgrades<br>
    Repairs <span class="dot">•</span> Maintenance
  </div>
  <div class="abs cta">CALL TODAY FOR A <strong>FREE</strong><br>NO OBLIGATION QUOTE</div>
  <div class="service-list">
    <ul class="col-left">
      <li>Lighting</li><li>LED lighting</li><li>Garden lighting</li><li>Ceiling fans</li>
      <li>Dimmers</li><li>Smoke detectors</li><li>Power points</li><li>Ovens and Cooktops</li>
    </ul>
    <ul class="col-right">
      <li>Telephone</li><li>Data</li><li>TV/Aerial</li><li>Switchboard upgrades</li>
      <li>Surge protectors</li><li>Hot Water Units</li><li>Test tagging</li><li>Safety switches (RCDS)<br>&nbsp;&nbsp;and Circuit breakers</li>
    </ul>
  </div>
  <div class="abs contact-name">LIAM CARTER - 0400 555 123</div>
  <div class="abs contact-email">keystonecurrent@example.com</div>
  <div class="abs legal">ABN 00 000 000 000 &nbsp;&nbsp; Lic 000000X<br>At Keystone Current we are fully insured and all work is completed to current Australian Electrical Standards</div>
</section>

<section class="flyer back">
  <div class="photo" role="img" aria-label="Photo of a bright modern white kitchen with LED downlights"></div>
  <div class="logo-plate">
    <span class="sq"></span>
    <span class="name">KEYSTONE<br>CURRENT<br>ELECTRICAL</span>
  </div>
  <div class="question-band">
    Are you spending too much on<br>your electricity bill?<br>Are you sick and tired of changing globes?
  </div>
  <div class="abs headline">SAVE UP TO $500 OFF YOUR<br>ELECTRICITY BILL</div>
  <div class="abs head-sub">Based on changing just 22 of your halogen downlights to LED</div>
  <div class="head-rule"></div>
  <div class="abs pitch">Why not save yourself some money while adding value to your house!<br>LEDs use at least 75% less electricity and last up to 50 times longer</div>

  <div class="table-title orange">YEARLY PRICES BASED ON 6 HOURS USE PER DAY @ $0.26 per kWh</div>
  <table class="data prices">
    <tr><th>NUMBER OF DOWNLIGHTS</th><th>HALOGEN GLOBE (50W)</th><th>LED (10W)</th><th>SAVINGS</th></tr>
    <tr><td>1</td><td>$28.47 per year</td><td>$5.69 per year</td><td>$22.78 per year</td></tr>
    <tr><td>10</td><td>$284.70</td><td>$56.90</td><td>$227.80</td></tr>
    <tr><td>20</td><td>$569.40</td><td>$113.80</td><td>$455.60</td></tr>
    <tr><td>30</td><td>$854.10</td><td>$170.70</td><td>$683.40</td></tr>
  </table>

  <div class="table-title dark">YEARLY REPLACEMENT COSTS BASED ON 6 HOURS USE PER DAY</div>
  <table class="data replace">
    <tr><th>NUMBER OF DOWNLIGHTS</th><th>HALOGEN (AV. 1000 HOURS)</th><th>LED (AV. 50000 HOURS)</th></tr>
    <tr><td>1</td><td>$8</td><td>$0</td></tr>
    <tr><td>10</td><td>$80</td><td>$0</td></tr>
    <tr><td>20</td><td>$160</td><td>$0</td></tr>
    <tr><td>30</td><td>$240</td><td>$0</td></tr>
  </table>

  <div class="abs more">Not just downlights, you can change any light to LED</div>
  <div class="light-types">
    <ul class="col-left"><li>Oyster lights</li><li>Spot lights</li><li>Pendant lights</li></ul>
    <ul class="col-right"><li>Directional lights</li><li>Wall lights</li><li>External lights</li></ul>
  </div>
</section>

</body>
</html>
```